Northcliff Thermal Services Ltd Needs a 2 sided A5 Flyer Design

We need a flyer design for our company to promote Air and ground Source Heat Pumps in the Devon and Cornwall region of the UK.

Our Government has launched the DWB (domestic warmth bonus) a 7 year quarterly payment to offset the cost of installation..
Homeowners currently using OIL or LPG gas for there heating and hot water will save up to 50% on there energy bill by swapping to a heat pump,
Currently education is needed to the potential end user on the benefits of heat pumps,
This flyer will be part of an initial start point to get the homeowner to book a free survey to discuss there options, We are a renewable energy company with great local knowledge, and a wealth of experience ......

KEY points SAVINGS OF UP TO 50% on OIL or LPG heating and hot water systems

DWB PAYMENTS FROM GOVERNMENT FOR 7 years

HONEST IMPARTIAL ADVICE ON SOLUTIONS

FREE SURVEYS ON ALL RENEWABLE SOLUTIONS AND COSTINGS. website www.ncthermal.co.uk have included some potential wording

LOGOS FROM SUPPLIERS

We think side one should be high impact on high oil and LPG gas costs, harm to environment and potential 50% savings with a heat pump. Side 2 to be DWB 7 year quarterly payment and a little about our company offering expertise and free impartial advice and survey

general theme a "striking call to action"

Target Market(s)

Target market is 40 to 60 year old home owners that are off gas grid and use oil or LPG for heating and hot water

Industry/Entity Type

Environment

Font styles to use
Serif
Sans Serif

Colors
33a6d7
f04a50
00a88f
fbed22

Requirements
Must have
• savings 50% on oil or LPG energy costs for heating and hot water

DWB (domestic warmth bonus) government backed payments to offset cost of instalation

7 year payments averaging £1000 a year

FREE impartial advice and surveys

```html
<!DOCTYPE html>
<html lang="en">
<head>
<meta charset="utf-8">
<title>Northcliff Thermal Services Ltd – Heat Pump Flyer</title>
<link href="https://fonts.googleapis.com/css2?family=Oswald:wght@300;400;500;600;700&display=swap" rel="stylesheet">
<style>
  :root{
    --backdrop:#000000;
    --paper:#ffffff;
    --brand-green:#5f9313;
    --deep-green:#2f5d08;
    --ring-green:#7cae1e;
    --lime:#c9e23c;
    --panel-blue:rgba(28,104,232,0.92);
    --link-blue:#2c5fcf;
    --accent-orange:#f28c1c;
    --alert-red:#d61f2c;
    --ink:#222222;
    --soft-ink:#3a3a3a;
    --rule:#c8c8c8;
  }
  *{box-sizing:border-box;margin:0;padding:0}
  html,body{width:1200px;height:812px;overflow:hidden;background:var(--backdrop)}
  body{font-family:'Oswald',sans-serif}
  .stage{position:absolute;left:0;top:0;width:1308px;height:885px;transform:scale(0.9174);transform-origin:0 0;background:var(--backdrop)}
  .page{position:absolute;background:var(--paper);overflow:hidden}
  .page--back{left:30px;top:30px;width:595px;height:827px}
  .page--front{left:685px;top:33px;width:592px;height:824px}
  .abs{position:absolute}

  /* footer */
  .footer-bar{position:absolute;left:0;right:0;bottom:0;height:42px;background:var(--brand-green);color:#fff;
    display:flex;justify-content:space-between;align-items:center;padding:0 22px 0 18px;font-size:18px;font-weight:400;letter-spacing:1px}

  /* back side */
  .landscape{left:0;top:0;width:595px;height:545px;
    background:linear-gradient(180deg,#2f7fe6 0%,#5aa2ee 30%,#a9cdf0 52%,#6aa83a 62%,#86c23e 80%,#5d9a25 100%)}
  .landscape-curve{left:0;top:0}
  .intro-panel{left:0;top:65px;width:537px;height:258px;background:var(--panel-blue);color:#fff;
    padding:12px 14px 0 20px;font-weight:300;font-size:14.6px;line-height:20.5px}
  .intro-panel p+p{margin-top:20px}
  .contact-note{left:34px;top:552px;width:530px;font-size:14.2px;font-weight:300;line-height:22px;color:var(--ink)}
  .contact-invite{left:34px;top:604px;font-size:16px;font-weight:300;color:var(--link-blue);white-space:nowrap}
  .office{top:655px;width:180px;font-size:14px;font-weight:300;line-height:22px;color:var(--soft-ink);font-style:normal}
  .office h3{font-size:16.5px;font-weight:400;color:var(--accent-orange);margin-bottom:1px}
  .office--head{left:36px}
  .office--west{left:226px;border-left:1px solid var(--rule);padding-left:23px;margin-left:-23px}
  .office--east{left:414px;border-left:1px solid var(--rule);padding-left:23px;margin-left:-23px}

  /* front side */
  .barrel-photo{left:0;top:0;width:592px;height:300px;
    background:linear-gradient(180deg,#c9c9c9 0%,#8e8e8e 45%,#4a4a4a 80%,#2a2a2a 100%)}
  .green-sweep{left:0;top:0}
  .headline{left:28px;top:62px;color:#fff;font-weight:600;font-size:47px;line-height:59px;letter-spacing:1px;
    text-shadow:0 2px 3px rgba(0,0,0,.45);white-space:nowrap}
  .product-title{right:280px;top:316px;text-align:right;font-weight:500;line-height:46px;white-space:nowrap;
    text-shadow:0 2px 3px rgba(0,0,0,.4)}
  .product-title .lead{color:var(--lime);font-size:31px}
  .product-title .main{color:#fff;font-size:36px}
  .heat-pump-photo{left:50px;top:422px;width:265px;height:245px;border-radius:4px;
    background:linear-gradient(135deg,#f4f6f6 0%,#dfe4e6 60%,#c3c9cc 100%)}
  .badge{position:absolute;border-radius:50%;background:var(--deep-green);border:5px solid var(--ring-green);
    color:#fff;display:flex;flex-direction:column;align-items:center;justify-content:center;text-align:center;line-height:1.1}
  .badge--grant{left:329px;top:264px;width:132px;height:132px;font-size:14px;font-weight:400}
  .badge--grant .big{font-size:48px;font-weight:600;line-height:44px}
  .badge--grant .big small{font-size:19px;font-weight:400}
  .badge--saving{left:447px;top:214px;width:132px;height:132px;font-size:11.5px;font-weight:400;color:var(--lime)}
  .badge--saving .big{font-size:40px;font-weight:500;color:#fff;line-height:44px}
  .badge--saving .big small{font-size:20px}
  .badge--saving .after{color:#fff;font-size:11px}
  .badge--advice{left:440px;top:349px;width:126px;height:126px;font-size:14.5px;font-weight:400;color:var(--lime)}
  .badge--advice .big{font-size:21px;font-weight:500;color:#fff}
  .survey-box{left:310px;top:490px;width:265px;height:114px;background:var(--alert-red);border-radius:8px;
    color:#fff;font-size:21.5px;font-weight:500;line-height:31px;text-align:right;padding:12px 20px 0 0;letter-spacing:.3px;white-space:nowrap}
  .supplier-strip{left:3px;top:692px;width:315px;height:62px;background:#f1f1f1;display:flex;align-items:center;gap:18px;padding-left:28px}
  .supplier{display:block}
  .supplier--ring{width:34px;height:34px;border-radius:50%;border:3px solid #9bb3c6}
  .supplier--red{width:76px;height:32px;background:#e2141d}
  .supplier--blue{width:96px;height:26px;border-radius:13px;background:#1f6fb6}
  .company-mark{left:352px;top:690px;width:230px;display:flex;align-items:center;gap:10px;color:var(--ink);
    font-size:22px;font-weight:400;line-height:25px}
  .company-mark .square{flex:none;width:34px;height:34px;background:var(--ring-green)}
</style>
</head>
<body>
<div class="stage">

  <section class="page page--back">
    <div class="abs landscape" role="img" aria-label="Photograph of a sunny blue sky over rolling green hills and trees"></div>
    <svg class="abs landscape-curve" width="595" height="827" viewBox="0 0 595 827" aria-hidden="true">
      <path d="M0 530 C 180 540 420 470 595 340 L595 827 L0 827 Z" fill="#ffffff"/>
      <path d="M0 530 C 180 540 420 470 595 340" fill="none" stroke="#4f8a14" stroke-width="5"/>
    </svg>
    <div class="abs intro-panel">
      <p>In October of 2014 the Government finalised the groundbreaking DWB domestic warmth bonus. We are the first country in the world to give payments to cover the install cost of renewable technology based around heating and hot water.</p>
      <p>At Northcliff Thermal Services we are in a unique position to advise you on the options open to you to replace your Oil and LPG boilers in favour of products that are 50% cheaper to run and are also kinder to the environment.</p>
      <p>We have 15 years experience in the Renewable Energy market and are not tied to one supplier or one technology. This puts us in a position to discuss ALL the options that are open to you to enable you to make a correct informed decision.</p>
    </div>
    <p class="abs contact-note">Call our Plymouth based office and asks to speak to Daniel our Energy Consultant or Owen Hartley our Technical Director and they will be pleased to inform you further.</p>
    <p class="abs contact-invite">Please get in touch and we are happy to give free impartial advice on options open to you.</p>
    <address class="abs office office--head">
      <h3>Head Office</h3>Unit 12 Harbourside Park<br>Ferris Lane<br>Plymouth, Devon<br>PL4 7QN
    </address>
    <address class="abs office office--west">
      <h3>South West</h3>Marlow Trading Estate<br>Ashby Road<br>Clevedon, Avon<br>BS21 6JR
    </address>
    <address class="abs office office--east">
      <h3>South East</h3>Unit 40<br>Greystone Business Park<br>Whitstable, Kent, CT5 2LW<br>South West
    </address>
    <footer class="footer-bar"><span>CALL : 01752 480193</span><span>WWW.NCTHERMAL.CO.UK</span></footer>
  </section>

  <section class="page page--front">
    <div class="abs barrel-photo" role="img" aria-label="Photograph of rows of grey oil drums"></div>
    <svg class="abs green-sweep" width="592" height="824" viewBox="0 0 592 824" aria-hidden="true">
      <path d="M0 285 C 180 265 400 230 592 150 L592 470 C 400 480 180 510 0 545 Z" fill="#5f9313"/>
      <path d="M230 265 C 380 240 500 200 592 160 L592 185 C 480 225 360 255 230 265 Z" fill="#2f5d08"/>
      <path d="M0 280 C 180 262 400 226 592 148" fill="none" stroke="#3f7410" stroke-width="6"/>
    </svg>
    <h1 class="abs headline">NO TO OIL<br>NO TO LPG</h1>

    <svg class="abs" style="left:275px;top:92px" width="146" height="146" viewBox="0 0 146 146" role="img" aria-label="Photograph of a spilling black oil barrel, crossed out">
      <defs><linearGradient id="oilTone" x1="0" y1="0" x2="1" y2="1"><stop offset="0" stop-color="#f2f2f2"/><stop offset="1" stop-color="#7a7a7a"/></linearGradient></defs>
      <circle cx="73" cy="73" r="68" fill="url(#oilTone)" stroke="#6fa31a" stroke-width="6"/>
      <path d="M38 40 L108 108 M108 40 L38 108" stroke="#e8141c" stroke-width="5"/>
    </svg>
    <svg class="abs" style="left:427px;top:33px" width="130" height="130" viewBox="0 0 130 130" role="img" aria-label="Photograph of a blue LPG gas bottle, crossed out">
      <defs><linearGradient id="gasTone" x1="0" y1="0" x2="1" y2="1"><stop offset="0" stop-color="#59b7e6"/><stop offset="1" stop-color="#1d6fb0"/></linearGradient></defs>
      <circle cx="65" cy="65" r="60" fill="url(#gasTone)" stroke="#6fa31a" stroke-width="6"/>
      <path d="M32 32 L98 98 M98 32 L32 98" stroke="#e8141c" stroke-width="5"/>
    </svg>

    <div class="badge badge--saving">save up to<div class="big">50<small>%</small></div><div class="after">ON YOUR ENERGY BILL<br>BY SWAPPING TO<br>A HEAT PUMP</div></div>
    <div class="badge badge--grant">DWB PAYMENTS<br>FROM<br>GOVERNMENT FOR<div class="big">7<small> years</small></div></div>
    <div class="badge badge--advice"><div class="big">HONEST</div>IMPARTIAL<br>ADVICE ON<br>SOLUTIONS</div>

    <h2 class="abs product-title"><span class="lead">AIR AND GROUND</span><br><span class="main">SOURCE HEAT PUMPS</span></h2>
    <div class="abs heat-pump-photo" role="img" aria-label="Photograph of a white air source heat pump unit with fan grille"></div>
    <div class="abs survey-box">FREE SURVEYS ON<br>ALL RENEWABLE<br>SOLUTIONS &amp; COSTINGS</div>

    <div class="abs supplier-strip" aria-label="Supplier and approved installer badges">
      <span class="supplier supplier--ring"></span>
      <span class="supplier supplier--red"></span>
      <span class="supplier supplier--blue"></span>
    </div>
    <div class="abs company-mark"><span class="square"></span><span>Northcliff Thermal Services Ltd</span></div>

    <footer class="footer-bar"><span>CALL : 01752 480193</span><span>WWW.NCTHERMAL.CO.UK</span></footer>
  </section>

</div>
</body>
</html>
```